Breezeway Climate Business Card Design

Design new, 2 sides, business cards for a residential and light commercial heating, air conditioning contractor.

Target Market(s)

Homeowners, small businesses

Industry/Entity Type

Business

Contact Information for Business Card

Dominic Vasquerelli
Phone - 555-214-6837
Email
Address - PO box 618
Millbrook NJ 07999
Website - www.BreezewayClimateLLC.example

Requirements
Must have
• logo, company colors, standard size with no die cut, so I can use printhaven

```html
<!DOCTYPE html>
<html lang="en">
<head>
<meta charset="utf-8">
<title>Breezeway Climate Business Card</title>
<link rel="stylesheet" href="https://fonts.googleapis.com/css2?family=Open+Sans:wght@400;600;700&display=swap">
<style>
  :root {
    --stage: #3a3a3c;
    --crimson: #9c1f33;
    --crimson-deep: #7e1526;
    --crimson-light: #b02a3f;
    --orange: #f39a1e;
    --cream: #fbe3b8;
    --ink: #3c3c3c;
    --rule: #d8d8d8;
    --paper: #ffffff;
  }
  * { box-sizing: border-box; margin: 0; padding: 0; }
  html, body { width: 1200px; height: 843px; overflow: hidden; }
  body {
    background: var(--stage);
    font-family: "Open Sans", Arial, sans-serif;
    display: flex;
    align-items: center;
    justify-content: center;
    gap: 44px;
  }
  .card {
    width: 540px;
    height: 309px;
    position: relative;
    flex: none;
    box-shadow: 0 10px 28px rgba(0,0,0,0.45);
  }
  .card-back {
    background: linear-gradient(135deg, var(--crimson-light), var(--crimson) 55%, var(--crimson-deep));
    display: flex;
    align-items: center;
    justify-content: center;
  }
  .brand {
    display: flex;
    align-items: center;
    gap: 12px;
  }
  .brand-dot {
    width: 22px;
    height: 22px;
    border-radius: 50%;
    background: var(--orange);
    flex: none;
  }
  .brand-name {
    font-weight: 700;
    font-size: 34px;
    letter-spacing: 0.5px;
    color: var(--cream);
  }
  .card-front {
    background: var(--paper);
    display: flex;
    align-items: center;
    padding: 0 22px 0 26px;
  }
  .card-front .brand { width: 212px; flex: none; }
  .card-front .brand-name {
    color: var(--crimson);
    font-size: 25px;
    line-height: 1.15;
  }
  .card-front .brand-dot { width: 18px; height: 18px; }
  .divider {
    width: 3px;
    flex: none;
    align-self: stretch;
    margin: 56px 18px 60px 8px;
    background: linear-gradient(var(--orange) 0 22%, var(--rule) 22% 100%);
  }
  .contact {
    color: var(--ink);
    font-size: 13px;
    line-height: 1.35;
    min-width: 0;
  }
  .person-name {
    color: var(--crimson);
    font-weight: 600;
    font-size: 18px;
    line-height: 1.2;
    white-space: nowrap;
  }
  .person-title { color: var(--orange); font-size: 13px; margin-bottom: 10px; }
  .address { margin-bottom: 10px; }
  .lines { list-style: none; }
  .lines li { white-space: nowrap; }
  .lines .label {
    color: var(--crimson);
    font-weight: 700;
    display: inline-block;
    width: 22px;
  }
  .web {
    margin-top: 10px;
    color: var(--crimson);
    font-weight: 600;
    letter-spacing: 0.4px;
    font-size: 11.5px;
    white-space: nowrap;
  }
</style>
</head>
<body>
  <section class="card card-back" aria-label="Card back">
    <div class="brand">
      <span class="brand-dot"></span>
      <span class="brand-name">Breezeway Climate</span>
    </div>
  </section>

  <section class="card card-front" aria-label="Card front">
    <div class="brand">
      <span class="brand-dot"></span>
      <span class="brand-name">Breezeway Climate</span>
    </div>
    <div class="divider"></div>
    <div class="contact">
      <p class="person-name">Dominic Vasquerelli</p>
      <p class="person-title">President</p>
      <p class="address">PO box 618<br>Millbrook NJ 07999</p>
      <ul class="lines">
        <li><span class="label">P:</span>555-214-6837</li>
        <li><span class="label">M:</span>555-309-4418</li>
        <li><span class="label">F:</span>555-782-1904</li>
        <li><span class="label">E:</span>dominic@mail.example</li>
      </ul>
      <p class="web">www.BreezewayClimateLLC.example</p>
    </div>
  </section>
</body>
</html>
```